Project Management Consultancy needs logo, business card and stationary design

I need a logo, business card and stationary design for a start-up project management consultancy servicing clients in corporate, education, aviation, local government and construction sectors.

The business will provide professional advice to clients and our people, knowledge and experience is essentially what we sell.

Our role is to assist our clients in delivering successful construction and transition projects whilst ensuring that their needs are identified, understood and achieved.

The company is small and provides a tailor made service for our clients. We pride ourselves on being
- professional
- innovative
- collaborative
- dependable
- communicative
- confident
- bold
The logo, business card and stationary should reflect this.

Can you please include the following on the stationary as appropriate.
Address:
17 Merrowind Close
Tarrabin
NSW 2593

ABN: 42 873 306 218

I very much look forward to receiving your designs.

Gareth P.

Target Market(s)

Corporate clients such as: airports, universities, government, financial organisations, etc.

Industry/Entity Type

Management Consulting

Contact Information for Business Card

Gareth Pellow
Director
Pellow Management Consulting Pty Ltd
e. gareth.pellow@pellow-mc.example.com.au
m. +61 455 318 906

Font styles to use
Other font styles liked:
• perhaps Arial Narrow? I am open to suggestions

Requirements
Must have
• An dynamic and corporate look and feel.
Should not have
• Should not be boring.

```html
<!DOCTYPE html>
<html lang="en">
<head>
<meta charset="utf-8">
<title>Pellow Management Consulting – Business Card</title>
<link rel="stylesheet" href="https://fonts.googleapis.com/css2?family=Roboto:wght@300;400;500;700&display=swap">
<style>
  :root {
    --bg: #e9e7e3;
    --card-white: #ffffff;
    --card-grey: #e4e4e4;
    --brand-blue: #2a9fd8;
    --brand-blue-deep: #1f7fc0;
    --band-blue: #2596cf;
    --ink-dark: #2b2b2d;
    --ink-text: #3a3a3a;
    --ink-light: #ffffff;
  }
  * { box-sizing: border-box; margin: 0; padding: 0; }
  html, body { width: 1200px; height: 1023px; overflow: hidden; }
  body {
    background: var(--bg);
    font-family: "Roboto", Arial, sans-serif;
    position: relative;
  }
  .card {
    position: absolute;
    width: 700px;
    height: 400px;
    border-radius: 18px;
    overflow: hidden;
    box-shadow: 0 10px 26px rgba(0,0,0,0.18);
  }

  /* Front */
  .card-front {
    left: 90px; top: 80px;
    background: linear-gradient(180deg, var(--card-white) 0%, var(--card-grey) 100%);
  }
  .brand {
    position: absolute; left: 46px; top: 52px;
    display: flex; align-items: center; gap: 20px;
  }
  .brand-dot {
    width: 64px; height: 64px; border-radius: 50%;
    background: var(--brand-blue);
  }
  .brand-name {
    color: var(--brand-blue);
    font-weight: 500;
    font-size: 27px;
    line-height: 1.2;
    border-left: 1px solid var(--brand-blue);
    padding-left: 14px;
  }
  .brand-name span { display: block; letter-spacing: 1.5px; }
  .person {
    position: absolute; right: 48px; top: 56px;
    text-align: right;
  }
  .person-name {
    color: var(--brand-blue);
    font-weight: 700;
    font-size: 27px;
    letter-spacing: 0.5px;
  }
  .person-role {
    color: var(--ink-text);
    font-size: 17px;
    letter-spacing: 1px;
    margin-top: 2px;
  }
  .divider {
    position: absolute; left: 46px; right: 48px; top: 178px;
    height: 1px; background: var(--brand-blue);
  }
  .contacts {
    position: absolute; left: 46px; top: 202px;
    list-style: none;
    font-size: 15.5px; font-weight: 300;
    color: var(--brand-blue-deep);
  }
  .contacts li { display: flex; align-items: center; gap: 12px; margin-bottom: 12px; }
  .contacts svg { width: 16px; height: 16px; flex: none; fill: var(--ink-dark); }
  .footer-band {
    position: absolute; left: 0; right: 0; bottom: 0; height: 46px;
  }
  .footer-band svg { display: block; width: 100%; height: 100%; }
  .abn {
    position: absolute; right: 34px; bottom: 14px;
    color: var(--ink-light);
    font-size: 13px; letter-spacing: 0.5px;
  }

  /* Back */
  .card-back {
    left: 410px; top: 540px;
    background: radial-gradient(ellipse at 70% 65%, #35b2df 0%, var(--band-blue) 45%, var(--brand-blue-deep) 100%);
    display: flex; align-items: center; justify-content: center;
  }
  .back-brand {
    display: flex; align-items: center; gap: 24px;
  }
  .back-dot {
    width: 70px; height: 70px; border-radius: 50%;
    background: var(--ink-light);
  }
  .back-name {
    color: var(--ink-light);
    font-weight: 500;
    font-size: 30px;
    line-height: 1.25;
    letter-spacing: 1px;
  }
  .back-name span { display: block; }
</style>
</head>
<body>

<section class="card card-front" aria-label="Business card front">
  <div class="brand">
    <div class="brand-dot"></div>
    <div class="brand-name">
      <span>Pellow Management</span>
      <span>Consulting Pty Ltd</span>
    </div>
  </div>

  <div class="person">
    <p class="person-name">Gareth Pellow</p>
    <p class="person-role">Director</p>
  </div>

  <div class="divider"></div>

  <ul class="contacts">
    <li>
      <svg viewBox="0 0 24 24" aria-hidden="true"><path d="M6.6 10.8a15 15 0 0 0 6.6 6.6l2.2-2.2c.3-.3.7-.4 1-.2 1.1.4 2.3.6 3.6.6.6 0 1 .4 1 1V20c0 .6-.4 1-1 1A17 17 0 0 1 3 4c0-.6.4-1 1-1h3.5c.6 0 1 .4 1 1 0 1.3.2 2.5.6 3.6.1.3 0 .7-.2 1z"/></svg>
      +61 455 318 906
    </li>
    <li>
      <svg viewBox="0 0 24 24" aria-hidden="true"><path d="M2 5h20v14H2zM3.5 6.5v.4l8.5 6 8.5-6v-.4z"/></svg>
      gareth.pellow@pellow-mc.example.com.au
    </li>
    <li>
      <svg viewBox="0 0 24 24" aria-hidden="true"><path d="M12 2a7 7 0 0 0-7 7c0 5 7 13 7 13s7-8 7-13a7 7 0 0 0-7-7zm0 9.5A2.5 2.5 0 1 1 12 6.5a2.5 2.5 0 0 1 0 5z"/></svg>
      17 Merrowind Close, Tarrabin, NSW 2593
    </li>
  </ul>

  <div class="footer-band">
    <svg viewBox="0 0 700 46" preserveAspectRatio="none" aria-hidden="true">
      <rect x="0" y="0" width="700" height="46" fill="var(--band-blue)"/>
      <polygon points="420,0 700,0 700,46 400,46 412,30 404,22 416,10" fill="var(--ink-dark)"/>
    </svg>
  </div>
  <p class="abn">ABN: 42 873 306 218</p>
</section>

<section class="card card-back" aria-label="Business card back">
  <div class="back-brand">
    <div class="back-dot"></div>
    <div class="back-name">
      <span>Pellow Management</span>
      <span>Consulting Pty Ltd</span>
    </div>
  </div>
</section>

</body>
</html>
```